Our Pantry Remedy

I am a pharmacist turn chef and my current website www.ourpantryremedy.example is in desperate need of a make over. I want to be able to add how to videos, photographs and have tabs. The tabs needed will be Home, About, Recipes, Health & Wellness, Services, Confidentiality, Affordability, Blog, Articles and Friday Cocktails. Eventually I will want a news letter, but do not want that now, only the ability to add it later. I will also want to add a market place tab later to sell merchandise and ebooks. The ability to navigate should be easy and not confusing and the ability to post should be easy. I will need social media Friendloop, Pinvora, zemlo plus, zemlo, Snapcove and chirpel. In addition I will need some direction on how to operate the site. Examples of website I like (but do not want to copy) are www.buildfinewell.example www.drpetermarvell.example. It is best for me to work with someone who can explain things simply.

Another website I think is nice is www.tbgalley.example  Thanks!

Target Market(s)

The business will be diving right into the delicious side of Key West’s good health as a personal chef, a culinary wellness coach, a wellness cooking teacher, a healthful caterer and a wellness host and entertainer.
The site needs to promote health with the art of food because I am convinced that health is best enhanced, maintained and recovered through nutritious eating and cuisine, and not through pills.
I will be infusing fresh recipes with a Key West flair in hopes to share my passion and insights into nutrition and health with residents and visitors alike. I want everyone to feel welcome to come in and join the fun.

Industry/Entity Type

Chef

Colors

Designer to choose colors to be used in the design.

Requirements
Must have
• Easy navigation, easy operation and posting and social media tools. Spam filters to keep the creeps away and important plugins that make it all work.
Nice to have
• Everything is nice to have

```html
<!DOCTYPE html>
<html lang="en">
<head>
<meta charset="utf-8">
<title>Our Pantry Remedy</title>
<link href="https://fonts.googleapis.com/css2?family=Yanone+Kaffeesatz:wght@300;400&family=Arimo:wght@400;700&display=swap" rel="stylesheet">
<style>
:root{
  --page:#e6e6e6;
  --panel:#ffffff;
  --ink:#333333;
  --muted:#8a8a8a;
  --nav:#7a7a7a;
  --brand-green:#3a8a4a;
  --accent:#d9534f;
  --rule:#e3e3e3;
  --caption:rgba(30,30,30,.82);
  --link:#3b5998;
}
*{box-sizing:border-box;margin:0;padding:0}
html,body{width:712px;height:1200px;overflow:hidden;background:var(--page)}
body{position:relative;font-family:"Arimo",Arial,sans-serif;color:var(--ink)}
.abs{position:absolute}
.display{font-family:"Yanone Kaffeesatz",sans-serif}

.logo{left:18px;top:24px;font-size:22px;color:var(--brand-green);font-weight:400}
.site-title{left:0;width:712px;text-align:center;top:12px;font-size:32px;font-weight:400;color:#3a3a3a}
.site-tagline{left:0;width:712px;text-align:center;top:50px;font-size:10px;color:var(--muted)}

.main-nav{left:7px;top:80px;width:698px;height:40px;background:var(--panel);display:flex;justify-content:center;align-items:center;gap:21px}
.main-nav a{font-family:"Yanone Kaffeesatz",sans-serif;font-size:10.5px;letter-spacing:.3px;text-transform:uppercase;color:var(--nav);text-decoration:none}

.hero{left:7px;top:130px;width:698px;height:251px;background:linear-gradient(120deg,#d4a46e 0%,#e8d9c4 30%,#8fae4a 50%,#cfc6bb 70%,#9a9c98 100%)}
.hero-caption{left:403px;top:262px;width:302px;height:119px}
.hero-caption svg{position:absolute;left:0;top:0}
.hero-caption h2{position:absolute;right:8px;top:34px;font-size:16px;color:#fff;font-weight:400;text-transform:uppercase}
.hero-caption p{position:absolute;right:8px;top:62px;width:276px;text-align:right;font-size:9px;line-height:12.5px;color:#fff}
.pager{right:24px;top:386px;display:flex}
.pager span{width:20px;text-align:center;font-size:10px;font-style:italic;color:var(--muted)}
.pager .on{color:var(--accent)}

.card{width:229px;height:237px;background:var(--panel);padding:0 10px}
.card h3{margin-top:16px;font-size:18px;line-height:18px;font-weight:400;color:#333;width:205px}
.card p{margin-top:7px;font-size:9.5px;line-height:12px;color:var(--muted);width:205px}
.card .thumb{position:absolute;left:10px;top:87px;width:199px;height:132px}

.widgets{left:7px;top:895px;width:698px;height:253px;background:var(--panel)}
.widget{position:absolute;top:22px;width:155px}
.widget h4{font-size:15px;font-weight:400;color:#333;margin-bottom:12px}
.entry{position:relative;padding:6px 0 6px;border-bottom:1px dotted #d6d6d6;min-height:58px}
.entry .mini{position:absolute;left:0;top:6px;width:36px;height:22px}
.entry b{display:block;margin-left:42px;font-family:"Yanone Kaffeesatz",sans-serif;font-weight:400;font-size:11px;line-height:12px;color:#444}
.entry span{display:block;font-size:8.5px;line-height:11px;color:var(--muted);text-indent:42px}

.social{position:absolute;left:535px;top:14px;width:156px}
.social .avatar{position:absolute;left:0;top:0;width:35px;height:35px;background:#8a6f9c}
.social .name{position:absolute;left:40px;top:2px;font-size:9.5px;font-weight:700;color:var(--link)}
.social .like{position:absolute;left:40px;top:15px;height:13px;padding:0 4px;font-size:8px;line-height:13px;background:var(--link);color:#fff}
.social .count{position:absolute;left:0;top:44px;font-size:7.5px;color:#555;width:156px;border-top:1px solid var(--rule);padding-top:5px}
.social .fans{position:absolute;left:0;top:62px;width:148px;height:148px;display:grid;grid-template-columns:repeat(4,34px);gap:4px}
.social .fans i{display:block;width:34px;height:34px}
.social .plug{position:absolute;left:0;top:216px;font-size:7.5px;color:#666;width:156px;border-top:1px solid var(--rule);padding-top:5px;display:flex;align-items:center;gap:4px}
.social .plug i{display:inline-block;width:8px;height:8px;background:var(--link)}

.footer{left:7px;top:1155px;width:698px;height:40px;background:var(--panel)}
.footer .copy{position:absolute;left:8px;top:10px;font-size:9.5px;color:#555}
.footer nav{position:absolute;left:346px;top:9px;width:345px;font-size:9.5px;line-height:12px;color:#555;white-space:nowrap}
.footer nav a{color:#555;text-decoration:none;margin-right:9px}
</style>
</head>
<body>

<header>
  <div class="abs logo display">Chef Reed Calder</div>
  <h1 class="abs site-title display">Our Pantry Remedy</h1>
  <p class="abs site-tagline">Better nutritional choices for positive healthy outcomes</p>
</header>

<nav class="abs main-nav">
  <a href="#">About</a><a href="#">Blog</a><a href="#">Recipes</a><a href="#">Health &amp; Wellness</a><a href="#">Services</a><a href="#">Confidentiality</a><a href="#">Affordability</a><a href="#">Blog</a><a href="#">Articles</a><a href="#">Friday Cocktails</a>
</nav>

<section class="abs hero" role="img" aria-label="Hands breaking broccoli over a pot beside chopped peppers"></section>
<div class="abs hero-caption">
  <svg width="302" height="119" viewBox="0 0 302 119"><polygon points="0,119 60,0 302,0 302,119" fill="var(--caption)"/></svg>
  <h2 class="display">Lorem Ipsum</h2>
  <p>Lorem Ipsum Dolor Sit Amet, Consectetur Adipiscing Elit. Nam Nec Rhoncus Risus. In Ultrices Lacinia Ipsum. In Ultrices Lacinia Ipsum. In Ultrices Lacinia Ipsum.</p>
</div>
<div class="abs pager"><span>1</span><span class="on">2</span><span>3</span></div>

<main>
  <article class="abs card" style="left:7px;top:408px">
    <h3 class="display">Meet the mineral in the shadows:<br>Magnesium</h3>
    <p>Most likely you are not sitting around wondering or fretting about your....</p>
    <div class="thumb" role="img" aria-label="Fresh fruits, vegetables and juices" style="background:linear-gradient(135deg,#7aa845,#d9534f 55%,#e9b93a)"></div>
  </article>
  <article class="abs card" style="left:242px;top:408px">
    <h3 class="display">Rocking Our Island’s Wellness<br>Factor</h3>
    <p>I am so happy to be back in Key West and I....</p>
    <div class="thumb" role="img" aria-label="Slicing mushrooms and tomatoes on a board" style="background:linear-gradient(135deg,#d8d0c4,#efe9e0 50%,#c65a3e)"></div>
  </article>
  <article class="abs card" style="left:476px;top:408px">
    <h3 class="display">The Bad Boys in Our Diet</h3>
    <p>After 8 months and a dozen columns, I am very happy to....</p>
    <div class="thumb" role="img" aria-label="Burger and fries on a plate" style="background:linear-gradient(135deg,#2b1a12,#b8742e 50%,#3a2418)"></div>
  </article>
  <article class="abs card" style="left:7px;top:651px">
    <h3 class="display">Super Chia Seeds</h3>
    <p>Good nutrition, wellness, healing, and longevity are common goals we all share....</p>
    <div class="thumb" role="img" aria-label="Bowls of vanilla chia seed pudding" style="background:linear-gradient(135deg,#d98a22,#c23a2e 50%,#e0a038)"></div>
  </article>
  <article class="abs card" style="left:242px;top:651px">
    <h3 class="display">FISH FOR DINNER</h3>
    <p>We are so lucky to have the ocean in our back yard....</p>
    <div class="thumb" role="img" aria-label="Grilled fish fillet with greens" style="background:linear-gradient(135deg,#dfe6ee,#c8865a 50%,#6f9a3c)"></div>
  </article>
  <article class="abs card" style="left:476px;top:651px">
    <h3 class="display">Hello world!</h3>
    <p>Welcome to PostPress. This is your first post. Edit or delete it,....</p>
    <div class="thumb" role="img" aria-label="Seared fish with salad" style="background:linear-gradient(135deg,#5a3a28,#c98a52 50%,#6b8f3a)"></div>
  </article>
</main>

<section class="abs widgets">
  <div class="widget" style="left:20px">
    <h4 class="display">New from the blog</h4>
    <div class="entry"><div class="mini" role="img" aria-label="Fish dish" style="background:#a9764a"></div><b>Hello world!</b><span>Welcome to PostPress. This is your first post. Edit or delete it,...</span></div>
    <div class="entry"><div class="mini" role="img" aria-label="Fruits and juices" style="background:#8aa646"></div><b>Meet the mineral in the shadows: Magnesium</b><span>Most likely you are not sitting around wondering or fretting about your...</span></div>
    <div class="entry"><div class="mini" role="img" aria-label="Chia pudding" style="background:#d4892a"></div><b>Super Chia Seeds</b><span>Good nutrition, wellness, healing, and longevity are common goals we all share...</span></div>
  </div>
  <div class="widget" style="left:190px">
    <h4 class="display">Popular Posts</h4>
    <div class="entry"><div class="mini" role="img" aria-label="Burger" style="background:#7a4a26"></div><b>The Bad Boys in Our Diet</b><span>After 8 months and a dozen columns, I am very happy to...</span></div>
    <div class="entry"><div class="mini" role="img" aria-label="Fruits and juices" style="background:#8aa646"></div><b>Meet the mineral in the shadows: Magnesium</b><span>Most likely you are not sitting around wondering or fretting about your...</span></div>
    <div class="entry"><div class="mini" role="img" aria-label="Fish dish" style="background:#a9764a"></div><b>Hello world!</b><span>Welcome to PostPress. This is your first post. Edit or delete it,...</span></div>
  </div>
  <div class="widget" style="left:359px">
    <h4 class="display">Popular Recipes</h4>
    <div class="entry"><div class="mini" role="img" aria-label="Burger" style="background:#7a4a26"></div><b>The Bad Boys in Our Diet</b><span>After 8 months and a dozen columns, I am very happy to...</span></div>
    <div class="entry"><div class="mini" role="img" aria-label="Fish dish" style="background:#a9764a"></div><b>Hello world!</b><span>Welcome to PostPress. This is your first post. Edit or delete it,...</span></div>
    <div class="entry"><div class="mini" role="img" aria-label="Fish fillet" style="background:#c8a98a"></div><b>FISH FOR DINNER</b><span>We are so lucky to have the ocean in our back yard...</span></div>
  </div>
  <div class="social">
    <div class="avatar" role="img" aria-label="Page picture"></div>
    <div class="name">The Pantry Remedy</div>
    <div class="like">Like</div>
    <div class="count">3,358 people like <span style="color:var(--link)">The Pantry Remedy</span>.</div>
    <div class="fans" role="img" aria-label="Grid of follower profile pictures">
      <i style="background:#c98a4e"></i><i style="background:#6a4a8c"></i><i style="background:#9a8a78"></i><i style="background:#d7b89a"></i>
      <i style="background:#3a3226"></i><i style="background:#6f6a66"></i><i style="background:#b07a6a"></i><i style="background:#8a4ac0"></i>
      <i style="background:#4a6a3a"></i><i style="background:#3f8a8a"></i><i style="background:#8a7a66"></i><i style="background:#7a90b4"></i>
      <i style="background:#e6d6e0"></i><i style="background:#e0b04a"></i><i style="background:#2a5a7a"></i><i style="background:#b86a3a"></i>
    </div>
    <div class="plug"><i></i>Friendloop social plugin</div>
  </div>
</section>

<footer class="abs footer">
  <p class="copy">All Rights Reserved 2014</p>
  <nav><a href="#">About</a><a href="#">Blog</a><a href="#">Recipes</a><a href="#">Health &amp; Wellness</a><a href="#">Services</a><a href="#">Confidentiality</a><br><a href="#">Affordability</a><a href="#">Blog</a><a href="#">Articles</a><a href="#">Friday Cocktails</a></nav>
</footer>

</body>
</html>
```